PaceUp

This app is built around three game modes—Quick Focus, Daily, and Calming—each offering short, low-stress interactions designed to prime focus, train cognitive skills, or regulate anxiety using neuroscience-informed mechanics. Gameplay spans spatial puzzles, word and memory challenges, and breathing or sensory experiences, all delivered in 1–5 minute routines with clean, calming UI patterns (grids, cards, breathing rings, soft animations). The goal is a cohesive system of micro-games and guided routines that enhance executive function, emotional regulation, and readiness before, during, or after high-stakes moments.

Colors
FFC000
F8CF3A
FAE287
FDF2CF
FEFAEE
F0912C
F2A743
F7CA91
FBE8D2
FDF5EE
EE7325
F08F49
F5BC92
FAE3D3
FDF4ED

```html
<!DOCTYPE html>
<html lang="en">
<head>
<meta charset="utf-8">
<title>PaceUp — App Screens</title>
<link href="https://fonts.googleapis.com/css2?family=Montserrat:ital,wght@0,500;0,600;0,700;0,800;1,500&family=Open+Sans:wght@400;500;600&display=swap" rel="stylesheet">
<style>
  :root{
    --page:#05060c;
    --navy-deep:#050d4f;
    --navy:#0a1c86;
    --navy-mid:#0d27a8;
    --cyan:#22cdf3;
    --cyan-soft:#5fe0ff;
    --cyan-pale:#a9f0ff;
    --ink:#06123e;
    --white:#ffffff;
    --chip-line:#3f6df0;
    --chip-fill:#16309c;
    --cell:#081550;
    --cell-line:#1a2c7c;
    --block:#2a7df0;
  }
  *{box-sizing:border-box;margin:0;padding:0}
  html,body{width:1200px;height:655px;overflow:hidden;background:var(--page)}
  body{position:relative;font-family:"Open Sans",sans-serif;color:var(--white)}

  .screen{
    position:absolute;top:57px;width:253px;height:542px;border-radius:30px;overflow:hidden;
    background:
      radial-gradient(ellipse 70% 45% at 50% 42%, rgba(40,90,230,.55), transparent 70%),
      linear-gradient(180deg,var(--navy-deep) 0%,var(--navy) 55%,var(--navy-deep) 100%);
  }
  .screen--home{left:113px}
  .screen--matrix{left:473px}
  .screen--mantra{left:834px}
  .abs{position:absolute}

  .status{position:absolute;top:8px;left:20px;right:18px;display:flex;justify-content:space-between;align-items:center;font:600 9.5px "Open Sans",sans-serif}
  .status svg{display:block}

  .app-title{position:absolute;left:0;right:0;text-align:center;font:700 24px "Montserrat",sans-serif;letter-spacing:.5px}
  .screen--home .app-title{top:28px}
  .game-title{position:absolute;left:0;right:0;top:32px;text-align:center;font:700 20px "Montserrat",sans-serif;letter-spacing:.3px}
  .remaining{position:absolute;left:0;right:0;top:61px;text-align:center;font:500 9px "Open Sans",sans-serif}

  /* streak */
  .streak{position:absolute;left:45px;top:98px;width:164px;height:164px;border-radius:50%;
    background:radial-gradient(circle at 50% 45%, #1ad0f2 0%, #11a8dd 45%, #0a63b8 78%, #0b3da0 100%);
    border:3px solid var(--cyan-pale);
    box-shadow:0 0 18px 6px rgba(60,210,255,.75),0 0 40px 14px rgba(40,140,255,.45), inset 0 0 16px 4px rgba(190,245,255,.8);
    text-align:center}
  .streak__label{position:absolute;left:0;right:0;top:34px;font:700 23px "Montserrat",sans-serif}
  .streak__count{position:absolute;left:0;right:0;top:58px;font:800 36px "Montserrat",sans-serif}
  .streak__sub{position:absolute;left:0;right:0;top:103px;font:400 15.5px "Open Sans",sans-serif}

  .mode{position:absolute;top:302px;width:70px;text-align:center}
  .mode svg{display:block;margin:0 auto}
  .mode__label{margin-top:8px;font:600 11px "Montserrat",sans-serif}

  .continue{position:absolute;left:17px;top:401px;width:221px;height:56px;border-radius:28px;
    background:linear-gradient(90deg,#12c3f0,#2fd8f8);color:var(--ink);box-shadow:0 0 14px rgba(40,200,255,.5)}
  .continue__title{position:absolute;left:25px;top:13px;font:600 11.5px "Montserrat",sans-serif}
  .continue__meta{position:absolute;left:25px;top:31px;font:400 7px "Open Sans",sans-serif;letter-spacing:-.2px}
  .resume{position:absolute;left:128px;top:17px;width:69px;height:23px;border-radius:12px;background:var(--ink);color:var(--white);
    font:700 10px "Montserrat",sans-serif;display:flex;align-items:center;justify-content:center}
  .tagline{position:absolute;left:0;right:0;top:465px;text-align:center;font:italic 500 8px "Montserrat",sans-serif}

  .tabbar{position:absolute;left:0;right:0;top:504px;height:30px}
  .tab{position:absolute;width:44px;margin-left:-22px;text-align:center;font:500 6.5px "Open Sans",sans-serif}
  .tab svg{display:block;margin:0 auto 3px}

  /* matrix */
  .halo{position:absolute;left:10px;top:94px;width:232px;height:232px;border-radius:50%;
    background:radial-gradient(circle, rgba(30,80,220,.5) 55%, rgba(30,80,220,.15) 72%, transparent 74%);
    box-shadow:inset 0 0 0 2px rgba(60,120,255,.35)}
  .pager{position:absolute;left:0;right:0;text-align:center}
  .board{position:absolute;left:41px;top:157px;width:171px;height:174px;display:grid;grid-template-columns:repeat(7,1fr);grid-template-rows:repeat(7,1fr);gap:2px;padding:2px;
    background:var(--cell-line);border:1px solid #2a44a8;box-shadow:0 0 20px rgba(20,40,140,.8)}
  .cell{background:var(--cell)}
  .cell--on{background:linear-gradient(180deg,#3aa0ff,#1e62e0);box-shadow:inset 0 0 0 1.5px var(--cyan-soft),0 0 6px rgba(80,180,255,.8)}
  .pieces{position:absolute;left:0;top:352px;width:253px;height:36px}

  .controls{position:absolute;left:15px;top:466px;width:223px;height:36px;border-radius:18px;
    background:linear-gradient(90deg,#1bc4f0,#2fd6f8);color:var(--ink);display:flex;justify-content:space-between;align-items:center;padding:0 16px 0 17px;
    font:600 11px "Montserrat",sans-serif}
  .controls span{display:flex;align-items:center;gap:4px}
  .home-bar{position:absolute;left:66px;top:534px;width:120px;height:3px;border-radius:2px;background:var(--white)}

  /* mantra */
  .mantra-card{position:absolute;left:16px;top:180px;width:222px;height:60px;border-radius:6px;
    background:linear-gradient(180deg,#1b3cb6,#142c94);border:1px solid #3d6cf0;box-shadow:0 0 14px rgba(40,90,230,.6);
    display:flex;align-items:center;justify-content:center;font:500 14.5px "Open Sans",sans-serif}
  .chip{position:absolute;width:66px;height:21px;border:1px solid var(--chip-line);background:var(--chip-fill);border-radius:2px;
    display:flex;align-items:center;justify-content:center;font:500 11px "Open Sans",sans-serif}
  .chip--picked{border:1.5px solid var(--cyan-soft);background:#1f48c8;box-shadow:0 0 6px rgba(80,200,255,.7)}
</style>
</head>
<body>

<!-- Home -->
<section class="screen screen--home">
  <div class="status"><span>9:45</span>
    <svg width="38" height="8" viewBox="0 0 38 8" fill="#fff"><rect x="0" y="5" width="2" height="3"/><rect x="3" y="3.5" width="2" height="4.5"/><rect x="6" y="2" width="2" height="6"/><rect x="9" y="0.5" width="2" height="7.5"/><path d="M14 3a6 6 0 0 1 8 0l-1 1a4.5 4.5 0 0 0-6 0zM16 5a3 3 0 0 1 4 0l-2 2z"/><rect x="26" y="1" width="10" height="6" rx="1.5"/></svg>
  </div>
  <svg class="abs" style="left:15px;top:38px" width="4" height="16" viewBox="0 0 4 16" fill="#fff"><circle cx="2" cy="2" r="1.7"/><circle cx="2" cy="8" r="1.7"/><circle cx="2" cy="14" r="1.7"/></svg>
  <h1 class="app-title">PACEUP</h1>
  <svg class="abs" style="left:223px;top:37px" width="16" height="18" viewBox="0 0 16 18" fill="none" stroke="#fff" stroke-width="1.4"><path d="M3 13V8a5 5 0 0 1 10 0v5l1.5 2h-13z"/><path d="M6.5 16.5a1.7 1.7 0 0 0 3 0"/></svg>

  <div class="streak">
    <div class="streak__label">STREAK</div>
    <div class="streak__count">7</div>
    <div class="streak__sub">Focus Ready</div>
  </div>

  <div class="mode" style="left:14px">
    <svg width="50" height="54" viewBox="0 0 50 54"><polygon points="25,2 47,14 47,40 25,52 3,40 3,14" fill="#1f6ee8" stroke="#3ad6ff" stroke-width="3"/><path d="M28 12 16 30h9l-3 12 12-18h-9z" fill="#fff"/></svg>
    <div class="mode__label">Quick Focus</div>
  </div>
  <div class="mode" style="left:94px">
    <svg width="50" height="54" viewBox="0 0 50 54"><polygon points="25,2 47,14 47,40 25,52 3,40 3,14" fill="#1f6ee8" stroke="#3ad6ff" stroke-width="3"/><rect x="16" y="18" width="18" height="17" rx="3" fill="#fff"/><rect x="19" y="15" width="2" height="5" fill="#fff"/><rect x="29" y="15" width="2" height="5" fill="#fff"/><path d="M20.5 27l3 3 6-6" stroke="#1f6ee8" stroke-width="2" fill="none"/></svg>
    <div class="mode__label">Daily</div>
  </div>
  <div class="mode" style="left:173px">
    <svg width="50" height="54" viewBox="0 0 50 54"><polygon points="25,2 47,14 47,40 25,52 3,40 3,14" fill="#1f6ee8" stroke="#3ad6ff" stroke-width="3"/><path d="M25 18c4 4 4 10 0 14-4-4-4-10 0-14zM14 24c6 0 9 4 11 8-6 0-10-3-11-8zM36 24c-6 0-9 4-11 8 6 0 10-3 11-8zM16 34h18" fill="#fff" stroke="#fff" stroke-width="1"/></svg>
    <div class="mode__label">Calming</div>
  </div>

  <div class="continue">
    <div class="continue__title">Continue</div>
    <div class="continue__meta">Mind Matrix - 45 sec left</div>
    <div class="resume">Resume</div>
  </div>
  <p class="tagline">Two minutes to lock in</p>

  <nav class="tabbar">
    <div class="tab" style="left:25px"><svg width="16" height="14" viewBox="0 0 16 14" fill="#3ad6ff"><path d="M8 0 0 7h2v7h4V9h4v5h4V7h2z"/></svg>Home</div>
    <div class="tab" style="left:77px"><svg width="18" height="14" viewBox="0 0 18 14" fill="#fff"><path d="M4 2h10a4 4 0 0 1 4 5l-1 5a2 2 0 0 1-3 1l-3-3H7l-3 3a2 2 0 0 1-3-1L0 7a4 4 0 0 1 4-5z"/><path d="M5 5v4M3 7h4" stroke="#0a1c86" stroke-width="1.3"/><circle cx="12.5" cy="6" r="1" fill="#0a1c86"/><circle cx="14" cy="8" r="1" fill="#0a1c86"/></svg>Games</div>
    <div class="tab" style="left:126px"><svg width="14" height="14" viewBox="0 0 14 14" fill="#fff"><rect width="6" height="6" rx="1"/><rect x="8" width="6" height="6" rx="1"/><rect y="8" width="6" height="6" rx="1"/><rect x="8" y="8" width="6" height="6" rx="1"/></svg>Routines</div>
    <div class="tab" style="left:179px"><svg width="14" height="14" viewBox="0 0 14 14" fill="#fff"><path d="M2 0h10v14l-5-4-5 4z"/></svg>Deck</div>
    <div class="tab" style="left:231px"><svg width="14" height="14" viewBox="0 0 14 14" fill="#fff"><circle cx="7" cy="4" r="4"/><path d="M0 14a7 5 0 0 1 14 0z"/></svg>Profile</div>
  </nav>
</section>

<!-- Mind Matrix -->
<section class="screen screen--matrix">
  <div class="status"><span>9:45</span>
    <svg width="38" height="8" viewBox="0 0 38 8" fill="#fff"><rect x="0" y="5" width="2" height="3"/><rect x="3" y="3.5" width="2" height="4.5"/><rect x="6" y="2" width="2" height="6"/><rect x="9" y="0.5" width="2" height="7.5"/><path d="M14 3a6 6 0 0 1 8 0l-1 1a4.5 4.5 0 0 0-6 0zM16 5a3 3 0 0 1 4 0l-2 2z"/><rect x="26" y="1" width="10" height="6" rx="1.5"/></svg>
  </div>
  <svg class="abs" style="left:20px;top:36px" width="9" height="15" viewBox="0 0 9 15" fill="none" stroke="#fff" stroke-width="2"><path d="M8 1 2 7.5 8 14"/></svg>
  <h1 class="game-title">MIND MATRIX</h1>
  <svg class="abs" style="left:219px;top:35px" width="20" height="17" viewBox="0 0 20 17" fill="none" stroke="#fff" stroke-width="1.3"><path d="M1 6h4l5-4v13l-5-4H1z"/><path d="M13 5a4 4 0 0 1 0 7M15.5 2.5a8 8 0 0 1 0 12"/></svg>
  <p class="remaining">Remaining 1:58</p>

  <div class="halo"></div>
  <svg class="pager" style="top:111px" width="253" height="6" viewBox="0 0 253 6"><circle cx="118" cy="3" r="2" fill="#fff"/><circle cx="126" cy="3" r="2" fill="#fff"/><circle cx="134" cy="3" r="2" fill="#fff"/></svg>

  <div class="board" role="grid" aria-label="Puzzle board">
    <i class="cell"></i><i class="cell"></i><i class="cell"></i><i class="cell"></i><i class="cell"></i><i class="cell"></i><i class="cell cell--on"></i>
    <i class="cell"></i><i class="cell"></i><i class="cell"></i><i class="cell"></i><i class="cell"></i><i class="cell cell--on"></i><i class="cell cell--on"></i>
    <i class="cell"></i><i class="cell cell--on"></i><i class="cell"></i><i class="cell"></i><i class="cell"></i><i class="cell"></i><i class="cell"></i>
    <i class="cell cell--on"></i><i class="cell cell--on"></i><i class="cell cell--on"></i><i class="cell"></i><i class="cell"></i><i class="cell"></i><i class="cell"></i>
    <i class="cell"></i><i class="cell"></i><i class="cell"></i><i class="cell"></i><i class="cell"></i><i class="cell"></i><i class="cell"></i>
    <i class="cell"></i><i class="cell"></i><i class="cell"></i><i class="cell"></i><i class="cell"></i><i class="cell"></i><i class="cell"></i>
    <i class="cell"></i><i class="cell"></i><i class="cell"></i><i class="cell"></i><i class="cell"></i><i class="cell"></i><i class="cell"></i>
  </div>

  <svg class="pieces" viewBox="0 0 253 36" fill="#1a4fd0" stroke="#5fe0ff" stroke-width="1.3">
    <rect x="44" y="1" width="11" height="11"/><rect x="55" y="1" width="11" height="11"/><rect x="66" y="1" width="11" height="11"/><rect x="55" y="12" width="11" height="11"/><rect x="55" y="23" width="11" height="11"/>
    <rect x="90" y="11" width="11" height="11"/><rect x="101" y="11" width="11" height="11"/>
    <rect x="131" y="4" width="14" height="14"/><rect x="145" y="4" width="14" height="14"/><rect x="131" y="18" width="14" height="14"/><rect x="145" y="18" width="14" height="14"/>
    <rect x="174" y="4" width="16" height="12"/><rect x="190" y="4" width="16" height="12"/><rect x="206" y="4" width="16" height="12"/>
  </svg>

  <div class="controls">
    <span><svg width="10" height="11" viewBox="0 0 10 11" fill="#06123e"><rect width="3" height="11"/><rect x="6" width="3" height="11"/></svg>Pause</span>
    <span>Next <svg width="8" height="12" viewBox="0 0 8 12" fill="none" stroke="#06123e" stroke-width="2"><path d="M1 1l5 5-5 5"/></svg></span>
  </div>
  <div class="home-bar"></div>
</section>

<!-- Mantra Make -->
<section class="screen screen--mantra">
  <div class="status"><span>9:45</span>
    <svg width="38" height="8" viewBox="0 0 38 8" fill="#fff"><rect x="0" y="5" width="2" height="3"/><rect x="3" y="3.5" width="2" height="4.5"/><rect x="6" y="2" width="2" height="6"/><rect x="9" y="0.5" width="2" height="7.5"/><path d="M14 3a6 6 0 0 1 8 0l-1 1a4.5 4.5 0 0 0-6 0zM16 5a3 3 0 0 1 4 0l-2 2z"/><rect x="26" y="1" width="10" height="6" rx="1.5"/></svg>
  </div>
  <svg class="abs" style="left:20px;top:36px" width="9" height="15" viewBox="0 0 9 15" fill="none" stroke="#fff" stroke-width="2"><path d="M8 1 2 7.5 8 14"/></svg>
  <h1 class="game-title">MANTRA MAKE</h1>
  <svg class="abs" style="left:219px;top:35px" width="20" height="17" viewBox="0 0 20 17" fill="none" stroke="#fff" stroke-width="1.3"><path d="M1 6h4l5-4v13l-5-4H1z"/><path d="M13 5a4 4 0 0 1 0 7M15.5 2.5a8 8 0 0 1 0 12"/></svg>
  <p class="remaining">Remaining 1:58</p>

  <div class="mantra-card">Calm sharp. Rise steady.</div>
  <svg class="pager" style="top:250px" width="253" height="5" viewBox="0 0 253 5" fill="#fff"><circle cx="108" cy="2.5" r="1.8"/><circle cx="115" cy="2.5" r="1.8"/><circle cx="122" cy="2.5" r="1.4" opacity=".7"/><circle cx="129" cy="2.5" r="1.4" opacity=".7"/><circle cx="136" cy="2.5" r="1.4" opacity=".7"/><circle cx="143" cy="2.5" r="1.4" opacity=".7"/></svg>

  <div class="chip" style="left:20px;top:270px">Sharp</div>
  <div class="chip" style="left:93px;top:270px">Rise</div>
  <div class="chip" style="left:165px;top:270px">Focus</div>
  <div class="chip" style="left:20px;top:301px">Ready</div>
  <div class="chip" style="left:93px;top:301px">Steady</div>
  <div class="chip chip--picked" style="left:165px;top:301px">Bold</div>
  <div class="chip chip--picked" style="left:60px;top:333px">Calm</div>
  <div class="chip" style="left:131px;top:333px">Strong</div>

  <div class="controls">
    <span><svg width="10" height="11" viewBox="0 0 10 11" fill="#06123e"><rect width="3" height="11"/><rect x="6" width="3" height="11"/></svg>Pause</span>
    <span>Next <svg width="8" height="12" viewBox="0 0 8 12" fill="none" stroke="#06123e" stroke-width="2"><path d="M1 1l5 5-5 5"/></svg></span>
  </div>
  <div class="home-bar"></div>
</section>

</body>
</html>
```